Rocket business card

Modern business card design, use of color is good with clean space too.

Things to include on card:

Quote: I add fuel to your optometry practice

- Eyewear Sales
- Admin Duties
- Revenue Collection
- Leadership
- Tech Adoption
- COGS Reduction
- Product Sourcing
-Medical Growth

Dalton Vessey, CEO
Glint Harbor
Text Me! 847-302-1964
dalton@glintharbor.example

```html
<!DOCTYPE html>
<html lang="en">
<head>
<meta charset="utf-8">
<title>Glint Harbor – Business Card</title>
<link rel="stylesheet" href="https://fonts.googleapis.com/css2?family=Open+Sans:wght@400;600;700&display=swap">
<style>
  :root {
    --stage: #2e2e2e;
    --card: #0b0b0c;
    --white: #ffffff;
    --orange: #f7931e;
    --red: #e8412c;
    --accent-line: #f26722;
  }
  * { box-sizing: border-box; margin: 0; padding: 0; }
  html, body {
    width: 1200px; height: 900px; overflow: hidden;
    background: var(--stage);
    font-family: "Open Sans", Arial, sans-serif;
    color: var(--white);
  }
  .stage {
    position: relative; width: 1200px; height: 900px;
    display: flex; flex-direction: column; align-items: center; justify-content: center; gap: 44px;
  }
  .card {
    position: relative;
    width: 660px; height: 377px;
    background: var(--card);
    border-radius: 26px;
    box-shadow: 0 12px 30px rgba(0,0,0,.45);
    overflow: hidden;
  }

  /* brand name block */
  .brand {
    display: flex; align-items: center; justify-content: center; gap: 14px;
  }
  .brand__dot {
    width: 46px; height: 46px; border-radius: 50%;
    background: var(--orange);
  }
  .brand__name {
    font-weight: 600; font-size: 34px; letter-spacing: 2px;
    color: var(--white); text-transform: uppercase;
  }

  /* front: services */
  .card--services .brand { margin-top: 74px; }
  .services__heading {
    display: flex; align-items: center; gap: 14px;
    margin: 44px 60px 16px;
  }
  .services__rule { flex: 1; height: 1px; background: var(--accent-line); }
  .services__title { font-weight: 700; font-size: 17px; letter-spacing: .5px; }
  .services__row {
    display: flex; justify-content: center; gap: 22px;
    font-size: 15px; letter-spacing: .4px; margin-bottom: 12px;
    list-style: none;
  }
  .services__row li::before {
    content: ""; display: inline-block; width: 6px; height: 6px; border-radius: 50%;
    background: var(--accent-line); margin-right: 6px; vertical-align: middle; position: relative; top: -2px;
  }

  /* back: contact */
  .card--contact { text-align: center; }
  .card--contact .brand { margin-top: 46px; }
  .contact__name {
    margin-top: 26px;
    font-weight: 700; font-size: 30px; letter-spacing: 1.5px; text-transform: uppercase;
    background: linear-gradient(90deg, var(--red), var(--orange));
    -webkit-background-clip: text; background-clip: text; color: transparent;
    display: inline-block;
  }
  .contact__role { font-size: 15px; margin-top: 2px; }
  .contact__divider {
    width: 18px; height: 3px; background: var(--accent-line); margin: 12px auto 10px;
  }
  .contact__prompt { font-size: 15px; }
  .contact__phone { font-size: 32px; font-weight: 600; letter-spacing: 1px; line-height: 1.2; }
  .contact__email {
    display: flex; align-items: center; justify-content: center; gap: 10px;
    font-size: 16px; margin-top: 6px;
  }
  .contact__email svg { width: 16px; height: 12px; }
</style>
</head>
<body>
<main class="stage">

  <section class="card card--services" aria-label="Card front – services">
    <div class="brand">
      <span class="brand__dot"></span>
      <span class="brand__name">Glint Harbor</span>
    </div>
    <div class="services__heading">
      <span class="services__rule"></span>
      <h2 class="services__title">Our Services</h2>
      <span class="services__rule"></span>
    </div>
    <ul class="services__row">
      <li>Eyewear Sales</li><li>Admin Duties</li><li>Revenue Collection</li><li>Leadership</li>
    </ul>
    <ul class="services__row">
      <li>Tech Adoption</li><li>COGS Reduction</li><li>Product Sourcing</li><li>Medical Growth</li>
    </ul>
  </section>

  <section class="card card--contact" aria-label="Card back – contact">
    <div class="brand">
      <span class="brand__dot"></span>
      <span class="brand__name">Glint Harbor</span>
    </div>
    <h1 class="contact__name">Dalton Vessey</h1>
    <p class="contact__role">CEO</p>
    <div class="contact__divider"></div>
    <p class="contact__prompt">Text Me!</p>
    <p class="contact__phone">847-302-1964</p>
    <p class="contact__email">
      <svg viewBox="0 0 16 12" aria-hidden="true">
        <rect x="0.5" y="0.5" width="15" height="11" fill="none" stroke="#f26722" stroke-width="1.4"/>
        <polyline points="1,1 8,7 15,1" fill="none" stroke="#f26722" stroke-width="1.4"/>
      </svg>
      dalton@glintharbor.example
    </p>
  </section>

</main>
</body>
</html>
```